Website Refresh for Brightfield Childcare

Company Overview:

Brightfield Childcare is a trusted provider of early childhood education and care services. We are dedicated to creating a nurturing environment where children can grow, learn, and thrive. Our centres offer a range of programs tailored to different age groups, and we pride ourselves on our commitment to quality, safety, and community engagement.

Project Overview:

We are looking for a talented designer to refresh our existing website (https://brightfieldchildcare.com.au/).

The primary goal is to modernize the design while keeping the content unchanged. The new design should be user-friendly, visually appealing, and reflective of our brand’s values. The website should share a similar "DNA" with our sister company’s website, Oak Harbour Early Learning, (https://oakharbourelc.com.au/) but it should not be a direct copy.

We want a design that mirrors our brand's shared values while introducing unique elements that distinguish Brightfield Childcare.

Design Requirements:
1. Home Page
2. About Us
3. Parent Info
4. Our Programs
5. Template for Centre Pages
6. Contact Us / Enrolment (Optional)

Design Style and Inspiration:
• The design should align with the "DNA" of Oak Harbour Early Learning, but also bring in unique design elements to set Brightfield Childcare apart.
• We are looking for a clean, modern, and professional design that is easy to navigate.
• The colour scheme and design elements should reflect our brand’s identity—welcoming, warm, and child-friendly without being overly childish.
• The design must be responsive, ensuring a great user experience across all devices, including desktops, tablets, and mobile phones.
• Accessibility is crucial—use clear fonts, sufficient contrast, and straightforward navigation.

Content Considerations:
• The content will remain the same; the focus is on enhancing the design and user interface.

Deliverables:
• High-fidelity mock-ups for each of the specified pages.
• Responsive design layouts for desktop, tablet, and mobile views.
• Design files should be delivered in a format compatible with any development team.

Target Audience:
• Parents of young children looking for childcare services.
• Community members interested in learning more about our centres and programs.

Submission Requirements:
• A brief explanation of your design approach and how it aligns with our branding goals.
• A portfolio showcasing your previous work, especially any similar projects.
• All requested deliverables must be included in your submission.

Judging Criteria:
• Alignment with our brand identity and the "DNA" of our sister company’s website.
• Visual appeal and user-friendliness of the design.
• Responsiveness and adaptability across different devices.
• Creativity and uniqueness in differentiating Brightfield Childcare from our sister company.

Notes:
• While we would like to engage the winning artist with the coding / css work, its not mandatory.
• Feel free to ask for any digital assets you need to complete the work.
• Main site to be refreshed - https://brightfieldchildcare.com.au/
• Sister site to take inspiration from - https://oakharbourelc.com.au/

Target Market(s)

A) Parents of young children looking for childcare services. B)Community members interested in learning more about our centres and programs.

Industry/Entity Type

Child Care

Number of Pages Required

5+ page

Requirements
Must have
• Please read description
Nice to have
• Please read description
Should not have
• Please read description

```html
<!DOCTYPE html>
<html lang="en">
<head>
<meta charset="UTF-8">
<title>Brightfield Childcare</title>
<link href="https://fonts.googleapis.com/css2?family=Poppins:wght@400;500;600&display=swap" rel="stylesheet">
<style>
:root{
  --sky:#87ceeb;
  --sky-deep:#5fb4dc;
  --sky-soft:#cfeaf6;
  --peach:#f6d6b8;
  --sun:#f7e6a8;
  --leaf:#bfe3c6;
  --ink:#333333;
  --card:#f7f8fa;
  --page:#f9f9f9;
  --white:#ffffff;
  --footer:#2c3e50;
}
*{box-sizing:border-box;margin:0;padding:0}
html,body{width:968px;height:1200px;overflow:hidden}
body{font-family:'Poppins',sans-serif;background:var(--page);color:var(--ink)}
.site-header{height:131px;background:var(--sky);text-align:center;padding-top:33px}
.brand{color:var(--white);font-size:25.5px;font-weight:600;line-height:1;margin-top:3px}
.main-nav{margin-top:23px;display:flex;justify-content:center;gap:30px}
.main-nav a{color:var(--white);text-decoration:none;font-size:14px;font-weight:600}
.hero{position:relative;height:258px;text-align:center;color:var(--white);overflow:hidden}
.hero-media{position:absolute;inset:0;
  background:
    radial-gradient(circle at 82% 30%, rgba(247,230,168,.9) 0, rgba(247,230,168,0) 38%),
    radial-gradient(ellipse at 15% 110%, rgba(191,227,198,.95) 0, rgba(191,227,198,0) 55%),
    linear-gradient(160deg, var(--sky-deep) 0%, #9ad3ea 45%, var(--peach) 100%);}
.hero-text{position:relative;padding-top:80px}
.hero h1{font-size:36px;font-weight:600;line-height:1.2;text-shadow:2px 2px 4px rgba(0,0,0,.4)}
.hero p{font-size:18px;margin-top:12px;text-shadow:1px 1px 3px rgba(0,0,0,.4)}
.content{width:938px;height:741px;margin:0 auto;background:var(--white);padding:56px 15px 0}
.section-title{color:var(--sky);font-size:24px;font-weight:600;line-height:1.2;margin-bottom:14px}
.body-text{font-size:12.9px;line-height:24px;margin-bottom:27px}
.programs{display:flex;gap:1px;margin-top:26px;margin-bottom:24px}
.program-card{width:302px;height:248px;background:var(--card);border-radius:6px;box-shadow:0 1px 4px rgba(0,0,0,.08);text-align:center;padding:14px 12px 0}
.program-media{width:76px;height:76px;border-radius:50%;margin:0 auto}
.media-infant{background:radial-gradient(circle at 35% 30%, #fdf0e2, var(--peach) 70%)}
.media-toddler{background:radial-gradient(circle at 35% 30%, #e7f6ea, var(--leaf) 70%)}
.media-preschool{background:radial-gradient(circle at 35% 30%, #eaf6fc, var(--sky) 75%)}
.program-card h3{font-size:18px;font-weight:600;margin-top:40px;line-height:1.2}
.program-card p{font-size:12.3px;line-height:19.5px;margin-top:12px}
.parent-text{margin-bottom:35px}
.cta{display:inline-block;background:var(--sky);color:var(--white);font-size:12px;font-weight:600;text-decoration:none;padding:0 15px;height:34px;line-height:34px;border-radius:3px}
.social{display:flex;justify-content:center;gap:15px;margin-top:23px}
.social span{width:30px;height:30px;border-radius:4px;background:var(--sky-soft);border:1px solid var(--sky)}
.site-footer{height:70px;background:var(--footer);color:var(--white);text-align:center;font-size:11px;line-height:70px}
</style>
</head>
<body>
<header class="site-header">
  <div class="brand">Brightfield Childcare</div>
  <nav class="main-nav">
    <a href="#">Home</a><a href="#">About Us</a><a href="#">Programs</a><a href="#">Parent Info</a><a href="#">Contact</a>
  </nav>
</header>
<section class="hero">
  <div class="hero-media" role="img" aria-label="Banner photo of children playing at the childcare centre"></div>
  <div class="hero-text">
    <h1>Welcome to Brightfield Childcare</h1>
    <p>Nurturing your child's growth and learning</p>
  </div>
</section>
<main class="content">
  <h2 class="section-title">About Us</h2>
  <p class="body-text">Brightfield Childcare is dedicated to creating a nurturing environment where children can thrive. We believe in providing high-quality early childhood education and care services that focus on the holistic development of every child.</p>
  <h2 class="section-title">Our Programs</h2>
  <div class="programs">
    <article class="program-card">
      <div class="program-media media-infant" role="img" aria-label="Infant care photo"></div>
      <h3>Infant Care</h3>
      <p>Our infant care program provides a safe and loving environment for your little one to explore and grow.</p>
    </article>
    <article class="program-card">
      <div class="program-media media-toddler" role="img" aria-label="Toddler program photo"></div>
      <h3>Toddler Program</h3>
      <p>Our toddler program is designed to encourage curiosity, learning, and the development of social skills.</p>
    </article>
    <article class="program-card">
      <div class="program-media media-preschool" role="img" aria-label="Preschool photo"></div>
      <h3>Preschool</h3>
      <p>Our preschool program prepares children for school through engaging activities and structured learning.</p>
    </article>
  </div>
  <h2 class="section-title">Parent Info</h2>
  <p class="body-text parent-text">We provide parents with all the information they need to ensure their child receives the best care and education possible. Our centers are transparent and open, and we value communication with our community.</p>
  <a class="cta" href="#">Contact Us for More Info</a>
  <div class="social" aria-label="Social links">
    <span role="img" aria-label="Social link"></span>
    <span role="img" aria-label="Social link"></span>
    <span role="img" aria-label="Social link"></span>
  </div>
</main>
<footer class="site-footer">© 2024 Brightfield Childcare. All rights reserved.</footer>
</body>
</html>
```